Contemporary Business card for Event Manager

Needed for my startup events company in Melbourne. Events I manage will be based within the fashion industry, sporting events, product launches etc. Not weddings or small dinner parties. Therfore I am after something professional and aimed at high end corporate market; but with the added emphasis on not being too conservative or boring. I am happy with a pop of colour e.g. yellow or copper foil.

Target Market(s)

fashion industry, design industry, high end sporting events e.g. Polo, Grand Prix, corporate clients,

Industry/Entity Type

Fashion

Contact Information for Business Card

side 1
Lena Varsby (can be upper or lower case, have a feature full stop between first and surname, or at the end of the nameetc) I am open to ideas. I would also be fine with my initials or name as a logo on the front (if this is the case my full name would need to go on the second side of the card.
2nd side:
Mobile: +61 491 570 156
email: lena.varsby@mailtrove.com.au

on one side of the card:
event management | brand activation | Advisory Services

Font styles to use
Serif
Sans Serif

Requirements
Must have
• side 2 must have
• mobile number
• email address
• event management | brand activation | Advisory Services
• ** my full name (Lena Varsby) must be on the card somewhere)
Nice to have
• 1st side
• I see the card stock being either a dark grey, light grey, natural white or black (all matt colours on unprocessed card). I see the writing being copper foil, or foil white or foil black.
• To give you a feel for me, think: contemporary, minimalist, I love line drawings, concrete, white with grey vein marble, copper, white, grey, black...yes I do like colour....yellow (but pops of colour) ;) I would like the card to look designer but 'on trend' as I deal with a lot of design and fashion clients....styles - think the sophistication and simplicity of Morvane or urban contemporary.
• some examples of what I like. Although please don't leet this limit you...I really am happy to have something a little more urban or design focused like a line drawing of an object, person too or a photo image too.
• https://www.moodfolia.com/pin/100000000000000001/
• https://www.moodfolia.com/pin/100000000000000002/
• https://www.moodfolia.com/pin/100000000000000003/
• https://www.moodfolia.com/pin/10000000000000004/
• https://www.moodfolia.com/pin/10000000000000005/
• https://www.moodfolia.com/pin/10000000000000006/
• https://www.moodfolia.com/pin/100000000000000007/
• https://www.moodfolia.com/pin/100000000000000008/
• https://www.moodfolia.com/pin/100000000000000009/
Should not have
• should not look commercial or have cartoonish looking logos. However happy with a simple line drawing or logo with initials etc.

```html
<!DOCTYPE html>
<html lang="en">
<head>
<meta charset="utf-8">
<title>Lena Varsby — Business Card</title>
<link rel="stylesheet" href="https://fonts.googleapis.com/css2?family=Cardo:wght@400&display=swap">
<style>
  :root {
    --backdrop: #5e5e5e;
    --card-stock: #ffffff;
    --ink: #2b2b2b;
    --copper: #b9824f;
    --copper-deep: #9a6436;
  }
  * { margin: 0; padding: 0; box-sizing: border-box; }
  html, body {
    width: 1200px;
    height: 676px;
    overflow: hidden;
  }
  body {
    background: var(--backdrop);
    display: flex;
    align-items: center;
    justify-content: center;
    font-family: "Cardo", "Palatino Linotype", Georgia, serif;
    color: var(--ink);
  }
  .business-card {
    width: 800px;
    height: 458px;
    background: var(--card-stock);
    box-shadow: 0 18px 40px rgba(0, 0, 0, 0.35);
    position: relative;
    display: flex;
    flex-direction: column;
    align-items: center;
  }
  .brand-mark {
    margin-top: 78px;
    display: flex;
    align-items: center;
    gap: 14px;
    font-size: 30px;
    letter-spacing: 0.12em;
    color: var(--copper);
  }
  .brand-mark__dot {
    width: 12px;
    height: 12px;
    border-radius: 50%;
    background: var(--copper);
  }
  .holder-name {
    margin-top: 40px;
    font-size: 50px;
    font-weight: 400;
    letter-spacing: 0.01em;
    line-height: 1;
  }
  .contact {
    margin-top: 34px;
    text-align: center;
    font-size: 19px;
    line-height: 1.35;
  }
  .services {
    position: absolute;
    left: 42px;
    right: 42px;
    bottom: 44px;
    display: flex;
    align-items: flex-end;
    list-style: none;
  }
  .services__item {
    flex: 1;
    font-size: 24px;
    padding: 0 10px 4px;
    border-bottom: 2px solid var(--copper);
    white-space: nowrap;
    text-align: center;
  }
  .services__item:first-child { text-align: left; padding-left: 0; }
  .services__item:last-child { text-align: right; padding-right: 0; }
  .services__divider {
    width: 2px;
    height: 30px;
    background: var(--copper-deep);
    flex: none;
  }
</style>
</head>
<body>
  <main class="business-card">
    <div class="brand-mark">
      <span class="brand-mark__dot"></span>
      <span class="brand-mark__name">Lena Varsby</span>
    </div>
    <h1 class="holder-name">Lena Varsby</h1>
    <p class="contact">
      <span class="contact__mobile">Mobile: +61 491 570 156</span><br>
      <span class="contact__email">E-mail: lena.varsby@mailtrove.com.au</span>
    </p>
    <ul class="services">
      <li class="services__item">Advisory Services</li>
      <li class="services__divider" aria-hidden="true"></li>
      <li class="services__item">Event Management</li>
      <li class="services__divider" aria-hidden="true"></li>
      <li class="services__item">Brand Activation</li>
    </ul>
  </main>
</body>
</html>
```